Anzeigengestaltung für Dienstleister für die professionelle Planung und Beschaffung von IT-Lösungen
Zielgruppe
Wir sind Dienstleister für die professionelle Planung und Beschaffung von IT-Lösungen.
Wir bieten umfassende und umfangreiche sowie produktneutrale Beratung zur Umsetzung Ihrer Digitalisierungsprojekte.
Unser Ziel ist es, Ihre individuellen Wünsche und Anforderungen mit speziell auf Sie abgestimmten Konzepten zu realisieren. Hierbei verstehen wir uns als Teamplayer, der alle Aspekte der verschiedenen Fachbereiche zu kombinieren versteht.
Fokus:
Neben den technischen Lösungen erarbeiten wir die detaillierten Anforderungen für Vergabeverfahren (öffentliche Ausschreibung national und EU weit)
Beratung
Planung
Erarbeiten von professionellen und produktneutralen Ausschreibungsunterlagen
Durchführen der Ausschreibung und Vergabe
Professionelle Dokumentation
Professionelle Projektbegleitung bis zur Abnahme und Abrechnung
Bereiche:
Digitalisierung Schulen
Rechenzentren
Telefon Lösungen
Druck Lösungen
Netzwerk und WLAN Lösungen
Zielkunden:
Öffentliche Kunde wie z.B. Kommunen, Schulen, Rathäuser, Hochschulen
Aufgabenstellung
OnePager A4 als Werbeflyer zur Darstellung meines Unternehmen, Neukundengewinnung

```html
<!DOCTYPE html>
<html lang="de">
<head>
<meta charset="utf-8">
<title>Sonnfeld – Digitalisierung mit uns</title>
<link rel="stylesheet" href="https://fonts.googleapis.com/css2?family=Ubuntu:wght@300;400&display=swap">
<style>
  :root {
    --green: #8dc21f;
    --navy: #1f1d4d;
    --text: #2b2b2b;
    --footer-bg: #ebebeb;
    --footer-dark: #555555;
    --white: #ffffff;
    --brand-ink: #2a2a2a;
  }
  html, body {
    margin: 0;
    padding: 0;
    overflow: hidden;
  }
  body {
    width: 928px;
    height: 1200px;
    position: relative;
    background: var(--white);
    font-family: "Ubuntu", sans-serif;
    color: var(--text);
  }
  .hero-visual {
    position: absolute;
    left: 0; top: 0;
    width: 928px; height: 563px;
    background:
      radial-gradient(ellipse 260px 90px at 330px 410px, rgba(80, 190, 255, 0.55), transparent 70%),
      radial-gradient(ellipse 280px 160px at 560px 300px, rgba(190, 120, 70, 0.55), transparent 70%),
      linear-gradient(180deg, #4b4e63 0%, #1d3a4f 35%, #0d2236 70%, #0a1522 100%);
  }
  .header-band {
    position: absolute;
    left: 0; top: 86px;
    width: 928px; height: 89px;
    display: flex;
  }
  .headline {
    width: 606px;
    background: var(--green);
    color: var(--white);
    font-weight: 300;
    font-size: 32px;
    margin: 0;
    display: flex;
    align-items: center;
    justify-content: flex-end;
    padding-right: 11px;
    box-sizing: border-box;
  }
  .brand {
    flex: 1;
    background: var(--white);
    display: flex;
    align-items: center;
    justify-content: center;
    color: var(--brand-ink);
    font-weight: 400;
    font-size: 32px;
  }
  .services {
    position: absolute;
    left: 96px; top: 529px;
    margin: 0; padding: 0;
    list-style: none;
    display: flex;
    gap: 18px;
    color: var(--white);
    font-size: 16px;
    letter-spacing: 2px;
  }
  .intro {
    position: absolute;
    left: 244px; top: 597px;
    width: 357px;
    margin: 0;
    font-weight: 300;
    font-size: 19px;
    line-height: 28.5px;
  }
  .intro-line {
    display: block;
    white-space: nowrap;
    text-align: justify;
    text-align-last: justify;
  }
  .intro-line.last {
    text-align: left;
    text-align-last: left;
  }
  .tagline {
    position: absolute;
    left: 244px; top: 906px;
    margin: 0;
    color: var(--navy);
    font-weight: 300;
    font-size: 34px;
  }
  .footer {
    position: absolute;
    left: 0; top: 1042px;
    width: 928px; height: 158px;
    background: var(--footer-bg);
  }
  .footer-url {
    position: absolute;
    left: 492px; top: 22px;
    color: var(--green);
    font-size: 30px;
    font-weight: 400;
  }
  .footer-panel {
    position: absolute;
    left: 488px; top: 79px;
    width: 440px; height: 79px;
    background: var(--footer-dark);
  }
  .footer-contact {
    position: absolute;
    top: 77px;
    margin: 0;
    font-style: normal;
    font-size: 11px;
    line-height: 16.3px;
    color: var(--text);
  }
  .footer-contact.company { left: 105px; }
  .footer-contact.people { left: 224px; }
</style>
</head>
<body>
  <div class="hero-visual" role="img" aria-label="Foto: Hand berührt ein leuchtendes digitales Netzwerk aus Lichtpunkten und Linien"></div>

  <header class="header-band">
    <h1 class="headline">Digitalisierung mit uns...</h1>
    <div class="brand">Sonnfeld</div>
  </header>

  <ul class="services">
    <li>BERATUNG</li>
    <li>PLANUNG</li>
    <li>DURCHFÜHRUNG</li>
    <li>BEGLEITUNG</li>
  </ul>

  <p class="intro">
    <span class="intro-line">Unser Ziel ist es, Ihre individuellen Wün-</span>
    <span class="intro-line">sche und Anforderungen mit speziell</span>
    <span class="intro-line">auf Sie abgestimmten Konzepten zu</span>
    <span class="intro-line">realisieren. Hierbei verstehen wir uns als</span>
    <span class="intro-line">Teamplayer, der alle Aspekte der ver-</span>
    <span class="intro-line">schiedenen Fachbereiche zu kombren</span>
    <span class="intro-line">versteht. Neben den technischen</span>
    <span class="intro-line">Lösungen erarbeiten wir die detaillier-</span>
    <span class="intro-line">ten Anforderungen für Ihr</span>
    <span class="intro-line last">Vergabeverfahren.</span>
  </p>

  <p class="tagline">.... die Zukunft kann kommen.</p>

  <footer class="footer">
    <div class="footer-url">sonnfeld-it.de</div>
    <div class="footer-panel"></div>
    <address class="footer-contact company">Sonnfeld GmbH<br>Lindenweg 14<br>88000 Musterstadt</address>
    <address class="footer-contact people">GF: Martin Keller<br>Tel: 07500 / 123456-0<br>&nbsp;info@sonnfeld-it.de</address>
  </footer>
</body>
</html>
```